Local snack brand needs a WordPress theme design

We need a custom WordPress theme for a new Australian snack company called Crunchwell. Based in Coffs Harbour, we create functional food snacks using local bananas and other produce. The theme should reflect our community-first philosophy and local roots, featuring an aerial banner of the region’s banana plantations and images of growers harvesting bananas.
The design should include layouts for:
1. Bio pages (profile photo and blurb)
2. Product pages (packaging, nutrition information panel, ingredients, 3. product description, health claim badges like “source of fibre” and “good source of potassium,” and awards)
4. Where to Buy page (interactive map, market stall imagery)
5. Blog posts (feature image, paragraph, quotes)
The final theme should use Crunchwell’s vector logo in the header (without text), and Crunchwell name (in brand font) in the footer. Should be modern, responsive design (mobile first). It should have a grass roots feel, be clean and feel good, leverage the brand colours, but still feel professional (to reflect a horticulturist and nutritionist), and be flexible for future updates. The successful design needs to be delivered as an installable theme in ZIP archive.
Please visit our website and read our pages to get a feel for "us". See https://crunchwell-example.au/
Updates
1 week extension for the 3 finalists to respond to feedback and make their final submissions before awarding 1st, 2nd and 3rd.
Target Market(s)
Local, health-conscious, athletes, busy parents, active minds
Industry/Entity Type
Food wholesaler, health & nutrition, agribusiness / local produce
Coding
Coded - Design and coding required
Font styles to use
Other font styles liked:
- Galano Grotesque Bold

```html
<!DOCTYPE html>
<html lang="en">
<head>
<meta charset="utf-8">
<title>Crunchwell – Dried Banana and Coconut Bites</title>
<link href="https://fonts.googleapis.com/css2?family=Poppins:wght@400;500;600;700;800&display=swap" rel="stylesheet">
<style>
:root{
  --green:#5b9a38;
  --green-dark:#4a8330;
  --ink:#111111;
  --text:#333333;
  --navy:#16294a;
  --white:#ffffff;
  --mist:#eef0ea;
}
*{box-sizing:border-box;margin:0;padding:0}
html,body{width:1200px;height:4253px;overflow:hidden}
body{font-family:'Poppins',sans-serif;color:var(--text);background:var(--white);position:relative}
section,header,footer{position:absolute;left:0;width:1200px}
.abs{position:absolute}
.center{left:0;width:1200px;text-align:center}
.btn{position:absolute;display:flex;align-items:center;justify-content:center;gap:8px;background:var(--green);color:var(--white);font-weight:600;font-size:15px;border-radius:24px;text-decoration:none}
.btn .dot{width:14px;height:14px;border-radius:50%;background:var(--white);display:inline-flex;align-items:center;justify-content:center}
.heading{font-weight:800;font-size:64px;letter-spacing:-1px;color:var(--ink);line-height:1}
.heading span{color:var(--green)}

/* header */
.site-header{top:0;height:160px;background:var(--white)}
.search{left:112px;top:20px;width:305px;height:50px;border:1px solid #ccc;border-radius:26px;box-shadow:0 2px 6px rgba(0,0,0,.15);display:flex;align-items:center;padding:0 22px;font-size:14px;color:#888;justify-content:space-between}
.stockist{left:883px;top:24px;width:204px;height:43px;font-size:14px}
.nav a{position:absolute;top:103px;font-size:17px;font-weight:500;color:var(--ink);text-decoration:none}
.nav a.active{color:var(--green)}
.brand-badge{left:503px;top:25px;width:194px;height:194px;border-radius:50%;background:var(--white);display:flex;align-items:center;justify-content:center;z-index:3}
.brand-badge b{color:var(--green);font-weight:700;font-size:26px}

/* hero */
.hero{top:160px;height:605px;background:linear-gradient(180deg,#3c6b22 0%,#4f7f2c 40%,#6c7d3a 70%,#7a5a33 100%)}
.play{left:578px;top:130px;width:56px;height:56px;border-radius:50%;background:var(--white);display:flex;align-items:center;justify-content:center}
.hero h1{top:226px;font-size:80px;line-height:80px;font-weight:800;color:var(--white);letter-spacing:1px}
.hero h2{top:322px;font-size:40px;line-height:50px;font-weight:700;color:var(--white)}

/* about */
.about{top:765px;height:656px}
.about .heading{top:122px}
.about p{font-size:15.5px;line-height:27.5px;color:var(--text)}

/* favourites */
.favourites{top:1421px;height:833px;background:linear-gradient(180deg,#e6e9e1,#f1f2ee 60%,#e3e6dd)}
.card{top:336px;width:297px;height:297px;background:var(--white);border-radius:6px;box-shadow:0 2px 8px rgba(0,0,0,.06)}
.pack{top:279px;width:210px;height:325px;border-radius:14px 14px 8px 8px;background:linear-gradient(180deg,#d8d8d6,#b9b9b6 30%,#c9a870 45%,#b8b8b4 70%,#a9a9a6)}
.pname{top:676px;width:297px;text-align:center;font-size:18px;font-weight:500;color:var(--ink)}
.arrow{top:456px;width:54px;height:54px;border-radius:50%;display:flex;align-items:center;justify-content:center}

/* why */
.why{top:2254px;height:452px}
.feature-icon{top:198px;width:72px;height:72px;border-radius:50%;background:#d9d9d9;display:flex;align-items:center;justify-content:center}
.feature-text{top:284px;width:360px;text-align:center;font-size:17px;font-weight:500;line-height:30px;color:var(--ink)}

/* find local */
.local{top:2706px;height:622px;background:linear-gradient(90deg,#5e6a47 0%,#6f8446 45%,#7c8f4a 70%,#55603a 100%)}
.local h2{left:110px;top:150px;font-size:66px;font-weight:800;color:var(--white);line-height:74px}
.local p{left:114px;top:322px;font-size:25px;line-height:36px;font-weight:600;color:var(--white)}

/* contact */
.contact{top:3328px;height:414px}
.contact p{top:195px;font-size:21px;font-weight:500;line-height:33px;color:var(--ink)}

/* footer */
.site-footer{top:3742px;height:511px;background:linear-gradient(180deg,#eceee8,#f3f4f0 50%,#e8eae3)}
.site-footer h4{font-size:18px;font-weight:600;color:var(--green)}
.site-footer ul{list-style:none;font-size:17.5px;line-height:33px;color:var(--ink)}
.divider{left:114px;top:297px;width:972px;height:1px;background:#bfc2b8}
</style>
</head>
<body>

<header class="site-header">
  <div class="abs search">Search For...
    <svg width="14" height="14" viewBox="0 0 14 14"><circle cx="6" cy="6" r="4.5" fill="none" stroke="#555" stroke-width="1.8"/><line x1="9.3" y1="9.3" x2="13" y2="13" stroke="#555" stroke-width="1.8"/></svg>
  </div>
  <nav class="nav">
    <a class="active" style="left:111px">Home</a>
    <a style="left:212px">Our Bio</a>
    <a style="left:320px">Our Product</a>
    <a style="left:763px">Where to Buy</a>
    <a style="left:931px">Blog</a>
    <a style="left:1015px">Contact</a>
  </nav>
  <div class="abs brand-badge"><b>Crunchwell</b></div>
  <a class="btn stockist"><svg width="10" height="14" viewBox="0 0 10 14"><path d="M5 0a5 5 0 0 0-5 5c0 4 5 9 5 9s5-5 5-9a5 5 0 0 0-5-5z" fill="#fff"/><circle cx="5" cy="5" r="1.8" fill="#5b9a38"/></svg>Stockist Locator</a>
</header>

<section class="hero" role="img" aria-label="Aerial view of a banana plantation with two growers harvesting bananas">
  <div class="abs play"><svg width="18" height="20" viewBox="0 0 18 20"><path d="M3 1l14 9-14 9z" fill="#111"/></svg></div>
  <h1 class="abs center">CRUNCHWELL</h1>
  <h2 class="abs center">Dried Banana and Coconut Bites</h2>
</section>

<section class="about">
  <h2 class="abs center heading">ABOUT <span>US</span></h2>
  <p class="abs center" style="top:213px">The science of functional snacking — grown, crafted and shared on the Coffs Coast.</p>
  <p class="abs" style="left:170px;width:860px;top:268px;text-align:center">We’re Sam &amp; Leo — a grower and a nutritionist — combining our love of real food and sustainable practice to create something a little different. Crunchwell is where fresh thinking meets rescued produce, and where small batches are made with big purpose.</p>
  <p class="abs" style="left:170px;width:860px;top:378px;text-align:center">From dehydrated bananas topped with coconut (our signature Cocobite), to chia fruit rolls and functional snack bars, everything we make starts with whole ingredients and is formulated to nourish. Designed for athletes, busy parents, active minds, and good eaters of all kinds.</p>
  <a class="btn" style="left:503px;top:499px;width:194px;height:42px">View More Bio <span class="dot"><svg width="6" height="8" viewBox="0 0 6 8"><path d="M1 1l3 3-3 3" stroke="#5b9a38" stroke-width="1.8" fill="none"/></svg></span></a>
</section>

<section class="favourites">
  <h2 class="abs center heading" style="top:106px">CLASSIC <span>FAVOURITES</span></h2>
  <p class="abs" style="left:180px;width:840px;top:195px;text-align:center;font-size:15.5px;line-height:27.5px">Every Crunchwell product is built from the ground up — using upcycled Australian-grown bananas and carefully selected wholefood ingredients.</p>

  <div class="abs card" style="left:114px"></div>
  <div class="abs card" style="left:451px"></div>
  <div class="abs card" style="left:788px"></div>
  <div class="abs pack" style="left:157px" role="img" aria-label="Cocobite product pouch"></div>
  <div class="abs pack" style="left:495px" role="img" aria-label="Cinnabite product pouch"></div>
  <div class="abs pack" style="left:832px" role="img" aria-label="Macabite product pouch"></div>
  <div class="abs pname" style="left:114px">COCOBITE</div>
  <div class="abs pname" style="left:451px">CINNABITE</div>
  <div class="abs pname" style="left:791px">MACABITE</div>

  <div class="abs arrow" style="left:37px;background:var(--green)"><svg width="14" height="12" viewBox="0 0 14 12"><path d="M7 1L2 6l5 5M12 1L7 6l5 5" stroke="#fff" stroke-width="1.8" fill="none"/></svg></div>
  <div class="abs arrow" style="left:1108px;background:var(--navy)"><svg width="14" height="12" viewBox="0 0 14 12"><path d="M2 1l5 5-5 5M7 1l5 5-5 5" stroke="#fff" stroke-width="1.8" fill="none"/></svg></div>

  <a class="btn" style="left:510px;top:714px;width:194px;height:42px">View More Info <span class="dot"><svg width="6" height="8" viewBox="0 0 6 8"><path d="M1 1l3 3-3 3" stroke="#5b9a38" stroke-width="1.8" fill="none"/></svg></span></a>
</section>

<section class="why">
  <h2 class="abs center heading" style="top:101px">WHY <span>CHOOSE US?</span></h2>
  <div class="abs feature-icon" style="left:205px"><svg width="40" height="40" viewBox="0 0 40 40" fill="none" stroke="#444" stroke-width="1.5"><circle cx="20" cy="20" r="17"/><path d="M12 15l8-4 8 4v10l-8 4-8-4z M12 15l8 4 8-4 M20 19v10"/></svg></div>
  <div class="abs feature-icon" style="left:564px"><svg width="40" height="40" viewBox="0 0 40 40" fill="none" stroke="#444" stroke-width="1.6"><path d="M16 8l-6 10h6M24 8l6 10M34 30H22l3-4M6 30l6-10M10 30h8"/></svg></div>
  <div class="abs feature-icon" style="left:922px"><svg width="42" height="36" viewBox="0 0 42 36" fill="none" stroke="#444" stroke-width="1.6"><path d="M4 16l8-8 6 2 4-6 6 4 4-2 6 10-2 10-8 6-6-2-4 2-4-4-6 0-4-6z"/></svg></div>
  <div class="abs feature-text" style="left:61px">Free from additives,<br>preservatives, or added sugar</div>
  <div class="abs feature-text" style="left:420px">Created with upcycled<br>produce to fight food waste</div>
  <div class="abs feature-text" style="left:778px">Made with Australian-grown<br>bananas (92% minimum)</div>
</section>

<section class="local" role="img" aria-label="Two growers exchanging freshly harvested bananas in a plantation">
  <h2 class="abs">FIND YOUR<br>LOCAL</h2>
  <p class="abs">Greenleaf Snack Foods stockist</p>
  <a class="btn" style="left:114px;top:392px;width:194px;height:44px">find stockist <span class="dot"><svg width="6" height="8" viewBox="0 0 6 8"><path d="M1 1l3 3-3 3" stroke="#5b9a38" stroke-width="1.8" fill="none"/></svg></span></a>
</section>

<section class="contact">
  <h2 class="abs center heading" style="top:109px">GET IN <span>TOUCH</span></h2>
  <p class="abs center">Got a question about our snacks, partnership opportunities, or bulk orders? Drop<br>us a message – our team is always happy to help.</p>
  <a class="btn" style="left:503px;top:291px;width:194px;height:42px">Contact With Us <span class="dot"><svg width="6" height="8" viewBox="0 0 6 8"><path d="M1 1l3 3-3 3" stroke="#5b9a38" stroke-width="1.8" fill="none"/></svg></span></a>
</section>

<footer class="site-footer">
  <div class="abs" style="left:110px;top:104px">
    <div style="font-size:21px;font-weight:700;color:var(--ink)">CRUNCHWELL</div>
    <p style="width:230px;margin-top:14px;font-size:15px;line-height:25px;color:var(--ink)">We’re Sam &amp; Leo — two locals passionate about real food, good soil, and better snacks.</p>
  </div>
  <div class="abs" style="left:407px;top:96px"><h4>Quick Links</h4><ul style="margin-top:8px"><li>Blog</li><li>About</li><li>FAQs</li><li>Authors</li></ul></div>
  <div class="abs" style="left:632px;top:96px"><h4>Other Links</h4><ul style="margin-top:8px"><li>Events</li><li>Shop</li><li>Patterns</li><li>Themes</li></ul></div>
  <div class="abs" style="left:861px;top:96px"><h4>Get Connectd</h4><ul style="margin-top:8px"><li>Follow the snack system.</li><li>Join the Crunchwell.</li><li>@crunchwell.au</li><li>Join our mailing list</li></ul></div>
  <div class="abs divider"></div>
  <p class="abs center" style="top:350px;font-size:15px;color:var(--ink)">Copyright@2025.All Rights Reserved</p>
</footer>

</body>
</html>
```